Artificial intelligence, machine learning, and automation company needs a sexy business card design

We need a sleek and sexy business card design for an AI consulting company based in Philadelphia PA. We provide custom machine learning and automation solutions for companies of all shapes and sizes. The primary industries that we serve are pharmaceuticals, engineering, healthcare, and computer software. We would like the designs to be a black business card that uses green as a sleek accent color. The final design should communicate intelligence, cutting edge new-tech, and optimization.

Target Market(s)

C-level and VP level executives of multi-million annual companies. Mostly in Pharma, Healthcare, Real Estate, Retail, and Engineering

Industry/Entity Type

Computer Software

Contact Information for Business Card

Name: Jack Moss
Title: CEO
Cell: 215 604 8293
Email: JackM@quillarcworks.example
Website: www.QuillarcWorks.example

Font styles to use
Sans Serif

Colors

Designer to choose colors to be used in the design.

Requirements
Must have
• 1) Attached Quillarc Logo (either with colors or not/embossed)
• 2) "Artificial Intelligence" "Automation" and "Machine Learning"
• 3) "Quillarc Laboratories" or "Quillarc Works" or "Quillarc"
• 4) Sexy AF.
Nice to have
• Black card / dark card color, "Quillarc Green" accent colors (in attached .ai file), Embossment of logo/name/etc, thick card stock, colored borders (on card sides, not front/back faces)
Should not have
• Should not be bland, or unsexy.

```html
<!DOCTYPE html>
<html lang="en">
<head>
<meta charset="utf-8">
<title>Quillarc Works – Business Card</title>
<link href="https://fonts.googleapis.com/css2?family=Bebas+Neue&display=swap" rel="stylesheet">
<style>
  :root {
    --paper: #ffffff;
    --card-black: #0b0b0b;
    --quillarc-green: #55c1ad;
    --deep-teal: #0f3b36;
    --signal-blue: #00aeef;
    --band-cyan: #12bcd4;
    --logo-grey: #4d4d4d;
  }
  * { box-sizing: border-box; margin: 0; padding: 0; }
  html, body { width: 1200px; height: 1200px; overflow: hidden; background: var(--paper); }
  body { position: relative; font-family: "Bebas Neue", "Arial Narrow", sans-serif; color: var(--quillarc-green); }

  .card {
    position: absolute; left: 206px; width: 804px;
    background: var(--card-black); overflow: hidden;
  }
  .card--front { top: 34px; height: 522px; }
  .card--back { top: 621px; height: 518px; }

  .card__layer { position: absolute; inset: 0; width: 100%; height: 100%; }

  .front__shade {
    position: absolute; left: 0; top: 0; bottom: 0; width: 260px;
    background: linear-gradient(90deg, #1c2020 0%, #101212 60%, rgba(11,11,11,0) 100%);
  }
  .front__edge-line {
    position: absolute; top: 0; bottom: 0; left: 6px; width: 12px;
    background: var(--quillarc-green);
  }
  .front__edge-line::after {
    content: ""; position: absolute; top: 0; bottom: 0; left: 4px; width: 2px; background: #0d2a26;
  }

  .brand-mark {
    position: absolute; display: flex; align-items: center; gap: 10px;
    color: var(--quillarc-green); font-family: "Bebas Neue", "Arial Narrow", sans-serif;
    letter-spacing: 2px; white-space: nowrap;
  }
  .brand-mark__square {
    width: 22px; height: 22px; border: 3px solid var(--quillarc-green); flex: none;
  }
  .brand-mark--front { left: 44px; top: 236px; font-size: 40px; }
  .brand-mark--back {
    left: 0; right: 0; top: 248px; justify-content: center; font-size: 44px; letter-spacing: 4px;
  }

  .holder__name {
    position: absolute; left: 271px; top: 44px; font-size: 86px; line-height: 1; letter-spacing: 1px;
  }
  .holder__title {
    position: absolute; left: 300px; top: 140px; font-size: 52px; line-height: 1;
  }

  .contact { position: absolute; display: flex; align-items: center; font-size: 35px; line-height: 1; white-space: nowrap; }
  .contact svg { flex: none; fill: var(--quillarc-green); }
  .contact--phone { left: 306px; top: 257px; gap: 19px; }
  .contact--email { left: 293px; top: 325px; gap: 18px; }
  .contact--web { left: 266px; top: 394px; gap: 20px; }
  .contact--address { left: 214px; top: 463px; gap: 18px; font-size: 33px; }

  .back__band { position: absolute; left: 0; right: 0; height: 13px;
    background: linear-gradient(180deg, #7fdde6 0%, var(--band-cyan) 35%, #0aa6c2 100%); }
  .back__band--top { top: 0; }
  .back__band--bottom { bottom: 0; }
</style>
</head>
<body>

<section class="card card--front" aria-label="Business card front">
  <div class="front__shade"></div>
  <svg class="card__layer" viewBox="0 0 804 522" aria-hidden="true">
    <defs>
      <linearGradient id="arcGradient" x1="0" y1="0" x2="0" y2="1">
        <stop offset="0" stop-color="#1aa7b8"/>
        <stop offset="0.5" stop-color="#0a8a80"/>
        <stop offset="1" stop-color="#00aeef"/>
      </linearGradient>
    </defs>
    <circle cx="15" cy="246" r="264" fill="none" stroke="url(#arcGradient)" stroke-width="20"/>
    <circle cx="15" cy="246" r="252" fill="none" stroke="#0b5552" stroke-width="2" opacity="0.7"/>
    <circle cx="990" cy="560" r="190" fill="none" stroke="var(--deep-teal)" stroke-width="18"/>
    <g stroke="var(--deep-teal)" stroke-width="5" fill="none" stroke-linecap="round">
      <line x1="804" y1="41" x2="732" y2="41"/>
      <polyline points="748,27 732,41 748,55"/>
    </g>
  </svg>
  <div class="front__edge-line"></div>

  <div class="brand-mark brand-mark--front">
    <span class="brand-mark__square"></span><span>Quillarc</span>
  </div>

  <h1 class="holder__name">JACK MOSS</h1>
  <p class="holder__title">CEO</p>

  <p class="contact contact--phone">
    <svg width="26" height="26" viewBox="0 0 24 24" aria-hidden="true"><path d="M6.6 10.8c1.4 2.8 3.8 5.1 6.6 6.6l2.2-2.2c.3-.3.7-.4 1-.2 1.1.4 2.3.6 3.6.6.6 0 1 .4 1 1V20c0 .6-.4 1-1 1C10.6 21 3 13.4 3 4c0-.6.4-1 1-1h3.5c.6 0 1 .4 1 1 0 1.3.2 2.5.6 3.6.1.3 0 .7-.2 1z"/></svg>
    <span>215 604 8293</span>
  </p>
  <p class="contact contact--email">
    <svg width="30" height="22" viewBox="0 0 30 22" aria-hidden="true"><path d="M0 0h30v2L15 12 0 2z"/><path d="M0 5l10 7-10 8zM30 5l-10 7 10 8zM12 13.5l3 2 3-2L29 22H1z"/></svg>
    <span>JACKM@QUILLARCWORKS.EXAMPLE</span>
  </p>
  <p class="contact contact--web">
    <svg width="20" height="30" viewBox="0 0 20 30" aria-hidden="true"><path d="M9 0v12H0V9a9 9 0 0 1 9-9zM11 0a9 9 0 0 1 9 9v3h-9zM0 14h20v7a9 9 0 0 1-9 9h-2a9 9 0 0 1-9-9z"/></svg>
    <span>WWW.QUILLARCWORKS.EXAMPLE</span>
  </p>
  <p class="contact contact--address">
    <svg width="22" height="30" viewBox="0 0 22 30" aria-hidden="true"><path d="M11 0A11 11 0 0 0 0 11c0 8 11 19 11 19s11-11 11-19A11 11 0 0 0 11 0zm0 15a4 4 0 1 1 0-8 4 4 0 0 1 0 8z"/></svg>
    <span>2750 LARCHMONT AVE, PHILADELPHIA, PA 19130</span>
  </p>
</section>

<section class="card card--back" aria-label="Business card back">
  <div class="back__band back__band--top"></div>
  <div class="back__band back__band--bottom"></div>

  <div class="brand-mark brand-mark--back">
    <span class="brand-mark__square"></span><span>Quillarc Laboratories</span>
  </div>

  <svg class="card__layer" viewBox="0 0 804 518" aria-hidden="true">
    <defs>
      <linearGradient id="arrowGradient" x1="0" y1="0" x2="0" y2="1">
        <stop offset="0" stop-color="#12bcd4"/>
        <stop offset="1" stop-color="#6fd7c8"/>
      </linearGradient>
    </defs>
    <rect x="748" y="340" width="6" height="166" fill="url(#arrowGradient)"/>
    <path d="M751 303 C757 330 768 345 782 352 C786 356 782 364 776 362 C766 356 757 350 751 346 C745 350 736 356 726 362 C720 364 716 356 720 352 C734 345 745 330 751 303 Z" fill="#12bcd4"/>
  </svg>
</section>

</body>
</html>
```